Innovative coffee bean bag design for roasters

We need a design which can be printed on a coffee bean bag but which could also work on a sticker of similar size. We're after quirky, geeky, playful and innovative. Something that will stand out and communicate the character of our business. It should be eye catching and draw the customer in for a closer look.
Thematically, think organic and earthy.
It needs an element which can be changed for different coffee origins and roast profiles, so the main design will remain the same but with a feature which changes to help the customer know what they're looking at and will make them smile.
Approximate dimensions we need are 15cm by 12cm, with the 15cm being the vertical height of the bag image. (The image will be viewed in portrait). This is the main print area - however, if you have a great idea for a full bag image (approximately 23cm by 13cm), feel free to submit this too, we're interested in all ideas.
There is an image attached of a white partially see-through bag which we are considering using, so keep this in mind when designing.
We will need our logo including - see attached image.
Finally, we need space for the information about the coffee, such as origin, roast profile, flavour notes - see attached image for an example of the information (not necessarily a stylistic indicator). Please suggest fonts etc.

Target Market(s)

coffee roasters

Requirements
Must have
• Must say under the logo coffee roasters( Tiny Kettle Organic Coffee Roasters )
Nice to have
• Unique symbol, shapes, scientific.

```html
<!DOCTYPE html>
<html lang="en">
<head>
<meta charset="utf-8">
<title>Tiny Kettle – Colombia bag labels</title>
<link href="https://fonts.googleapis.com/css2?family=Abril+Fatface&family=Arimo:wght@400;700&family=Roboto+Condensed:wght@700&display=swap" rel="stylesheet">
<style>
  :root {
    --backdrop: #a8a8a8;
    --paper: #ffffff;
    --ink: #1e1e1e;
    --rule: #2a2a2a;
    --brand-green: #5a9e32;
    --orange: #fd623e;   --orange-band: #ee5234;   --orange-line: #ff9c82;
    --yellow: #feb53a;   --yellow-band: #f4a82a;   --yellow-line: #ffd27f;
    --green: #74c14b;    --green-band: #64b23f;    --green-line: #a6dc86;
    --blue: #8dbcde;     --blue-band: #7aaed6;     --blue-line: #c1dbee;
  }
  * { box-sizing: border-box; margin: 0; padding: 0; }
  html, body { width: 1200px; height: 800px; overflow: hidden; }
  body {
    background: var(--backdrop);
    display: flex;
    align-items: center;
    justify-content: center;
    gap: 24px;
  }
  .bag-label {
    width: 270px;
    height: 476px;
    display: flex;
    flex-direction: column;
    background: var(--paper);
  }
  .bag-label--orange { --tone: var(--orange); --band: var(--orange-band); --line: var(--orange-line); }
  .bag-label--yellow { --tone: var(--yellow); --band: var(--yellow-band); --line: var(--yellow-line); }
  .bag-label--green  { --tone: var(--green);  --band: var(--green-band);  --line: var(--green-line); }
  .bag-label--blue   { --tone: var(--blue);   --band: var(--blue-band);   --line: var(--blue-line); }

  .brand-panel {
    height: 233px;
    background: var(--tone);
    color: var(--paper);
    display: flex;
    flex-direction: column;
    align-items: center;
    justify-content: center;
    gap: 8px;
    font-family: "Abril Fatface", serif;
    text-align: center;
  }
  .brand-dot {
    width: 46px; height: 46px;
    border-radius: 50%;
    background: var(--paper);
  }
  .brand-name { font-size: 27px; line-height: 1; letter-spacing: 1px; text-transform: uppercase; }
  .brand-tagline { font-size: 13px; line-height: 1.1; letter-spacing: .5px; }

  .origin-band {
    height: 179px;
    position: relative;
    background: var(--band);
  }
  .origin-card {
    position: absolute;
    top: 25px; left: 26px; right: 26px;
    height: 126px;
    background: var(--paper);
    display: flex;
    padding: 8px 12px 8px 8px;
  }
  .origin-name {
    width: 28px;
    border-right: 1.5px solid var(--rule);
    display: flex;
    align-items: center;
    justify-content: center;
  }
  .origin-name span {
    transform: rotate(-90deg);
    font-family: "Roboto Condensed", sans-serif;
    font-weight: 700;
    font-size: 19px;
    letter-spacing: 1.5px;
    color: var(--ink);
    white-space: nowrap;
  }
  .coffee-facts {
    flex: 1;
    display: grid;
    grid-template-columns: 1fr 1fr;
    grid-template-rows: 1fr 1fr 1fr;
    padding-left: 12px;
    font-family: "Arimo", sans-serif;
    color: var(--ink);
  }
  .fact { display: flex; flex-direction: column; justify-content: center; font-size: 6.5px; line-height: 1.05; }
  .fact dt { font-weight: 400; text-transform: uppercase; }
  .fact dd { font-weight: 700; text-transform: uppercase; }
  .fact--ruled { border-bottom: 1px solid var(--rule); }

  .band-stripe {
    height: 8px;
    background: var(--tone);
    border-top: 2px solid var(--line);
    border-bottom: 2px solid var(--band);
  }
  .label-footer {
    flex: 1;
    display: flex;
    align-items: center;
    justify-content: center;
    font-family: "Abril Fatface", serif;
    font-size: 20px;
    letter-spacing: 1px;
    color: var(--brand-green);
    text-transform: uppercase;
  }
</style>
</head>
<body>

  <article class="bag-label bag-label--orange">
    <header class="brand-panel">
      <div class="brand-dot"></div>
      <div class="brand-name">Tiny Kettle</div>
      <div class="brand-tagline">Organic Coffee Roasters</div>
    </header>
    <section class="origin-band" role="img" aria-label="Woven geometric pattern in deep orange">
      <div class="origin-card">
        <div class="origin-name"><span>COLOMBIA</span></div>
        <dl class="coffee-facts">
          <div class="fact fact--ruled"><dt>Process:</dt><dd>Washed</dd></div>
          <div class="fact fact--ruled"><dt>Varieties:</dt><dd>Caturra</dd></div>
          <div class="fact fact--ruled"><dt>Farm:</dt><dd>El Mirador</dd></div>
          <div class="fact fact--ruled"><dt>Producer:</dt><dd>Andres Molina</dd></div>
          <div class="fact"><dt>Location:</dt><dd>Huila</dd></div>
          <div class="fact"><dt>Roast</dt><dt>Date:</dt></div>
        </dl>
      </div>
    </section>
    <div class="band-stripe"></div>
    <footer class="label-footer">Tiny Kettle</footer>
  </article>

  <article class="bag-label bag-label--yellow">
    <header class="brand-panel">
      <div class="brand-dot"></div>
      <div class="brand-name">Tiny Kettle</div>
      <div class="brand-tagline">Organic Coffee Roasters</div>
    </header>
    <section class="origin-band" role="img" aria-label="Woven geometric pattern in deep yellow">
      <div class="origin-card">
        <div class="origin-name"><span>COLOMBIA</span></div>
        <dl class="coffee-facts">
          <div class="fact fact--ruled"><dt>Process:</dt><dd>Washed</dd></div>
          <div class="fact fact--ruled"><dt>Varieties:</dt><dd>Caturra</dd></div>
          <div class="fact fact--ruled"><dt>Farm:</dt><dd>El Mirador</dd></div>
          <div class="fact fact--ruled"><dt>Producer:</dt><dd>Andres Molina</dd></div>
          <div class="fact"><dt>Location:</dt><dd>Huila</dd></div>
          <div class="fact"><dt>Roast</dt><dt>Date:</dt></div>
        </dl>
      </div>
    </section>
    <div class="band-stripe"></div>
    <footer class="label-footer">Tiny Kettle</footer>
  </article>

  <article class="bag-label bag-label--green">
    <header class="brand-panel">
      <div class="brand-dot"></div>
      <div class="brand-name">Tiny Kettle</div>
      <div class="brand-tagline">Organic Coffee Roasters</div>
    </header>
    <section class="origin-band" role="img" aria-label="Woven geometric pattern in deep green">
      <div class="origin-card">
        <div class="origin-name"><span>COLOMBIA</span></div>
        <dl class="coffee-facts">
          <div class="fact fact--ruled"><dt>Process:</dt><dd>Washed</dd></div>
          <div class="fact fact--ruled"><dt>Varieties:</dt><dd>Caturra</dd></div>
          <div class="fact fact--ruled"><dt>Farm:</dt><dd>El Mirador</dd></div>
          <div class="fact fact--ruled"><dt>Producer:</dt><dd>Andres Molina</dd></div>
          <div class="fact"><dt>Location:</dt><dd>Huila</dd></div>
          <div class="fact"><dt>Roast</dt><dt>Date:</dt></div>
        </dl>
      </div>
    </section>
    <div class="band-stripe"></div>
    <footer class="label-footer">Tiny Kettle</footer>
  </article>

  <article class="bag-label bag-label--blue">
    <header class="brand-panel">
      <div class="brand-dot"></div>
      <div class="brand-name">Tiny Kettle</div>
      <div class="brand-tagline">Organic Coffee Roasters</div>
    </header>
    <section class="origin-band" role="img" aria-label="Woven geometric pattern in deep sky blue">
      <div class="origin-card">
        <div class="origin-name"><span>COLOMBIA</span></div>
        <dl class="coffee-facts">
          <div class="fact fact--ruled"><dt>Process:</dt><dd>Washed</dd></div>
          <div class="fact fact--ruled"><dt>Varieties:</dt><dd>Caturra</dd></div>
          <div class="fact fact--ruled"><dt>Farm:</dt><dd>El Mirador</dd></div>
          <div class="fact fact--ruled"><dt>Producer:</dt><dd>Andres Molina</dd></div>
          <div class="fact"><dt>Location:</dt><dd>Huila</dd></div>
          <div class="fact"><dt>Roast</dt><dt>Date:</dt></div>
        </dl>
      </div>
    </section>
    <div class="band-stripe"></div>
    <footer class="label-footer">Tiny Kettle</footer>
  </article>

</body>
</html>
```